Theme for 60th Anniversary party for a Business

We are looking for a theme for our 60th year party. The theme we used for our 50th party was a movie premier with a drive-in movie. Info on our 50th party is here http://corvelfield.com/about/50th-anniversary/. The theme must incorporate what we do as a business. Full website at www.corvelfield.com. The theme would be expanded upon with the use of props or other items to make a large celebration. The party would have around 400 invited guests to take place at our business location on an airport. Please provide details of your theme along with potential props, activities, or other items that would make your theme work. A logo for the theme will also be needed and could be provided with the theme.
Updates

Reason: Thanksgiving will be out thru the weekend.

Reason: Didn't have time for all family members to view and vote on entries.

Target Market(s)

Customers, Vendors, Potential Customers

Industry/Entity Type

Movie

Requirements
Must have
• Activities that can take place during event.

```html
<!DOCTYPE html>
<html lang="en">
<head>
<meta charset="utf-8">
<title>Fly With Us – 60th Anniversary Party Theme</title>
<link rel="stylesheet" href="https://fonts.googleapis.com/css2?family=Didact+Gothic&display=swap">
<style>
  :root {
    --paper: #ffffff;
    --ink: #1b1b1b;
    --line: 23.4px;
  }
  * { margin: 0; padding: 0; box-sizing: border-box; }
  html, body {
    width: 849px;
    height: 1200px;
    overflow: hidden;
    background: var(--paper);
  }
  .theme-sheet {
    position: relative;
    width: 849px;
    height: 1200px;
    padding: 76px 0 0 79px;
    font-family: "Didact Gothic", "Century Gothic", sans-serif;
    font-size: 18.3px;
    line-height: var(--line);
    color: var(--ink);
  }
  .section { margin-bottom: var(--line); }
  .section-title { font-weight: 400; font-size: inherit; text-transform: uppercase; }
  .section-body { white-space: nowrap; }
</style>
</head>
<body>
<main class="theme-sheet">
  <section class="section">
    <h2 class="section-title">Concept:</h2>
    <p class="section-body">Fly with us.</p>
  </section>

  <section class="section">
    <h2 class="section-title">Theme:</h2>
    <p class="section-body">Baording and flight theme. Everything would be like a flight.</p>
  </section>

  <section class="section">
    <h2 class="section-title">Invite:</h2>
    <p class="section-body">A beautiful, amybe vintage looking, boarding pass / passport to the<br>party - a funfilled destination. The invite could also give you an ETA<br>and ETD and you could have to check in at the counter as if you were<br>boarding a plane. Invite would have baggage tags wihch you would<br>have to collect.</p>
  </section>

  <section class="section">
    <h2 class="section-title">Arrival:</h2>
    <p class="section-body">On arrival - go to a check in counter and receive your baggage- a<br>small cardboard suitace with a few fun goodies like stickers (and other<br>corporate items), branded pen, hats, glasses fun things to wear and<br>have photos in and a raffle ticket</p>
  </section>

  <section class="section">
    <h2 class="section-title">Decor:</h2>
    <p class="section-body">large maps, globes hanging from the ceiling</p>
  </section>

  <section class="section">
    <h2 class="section-title">Music:</h2>
    <p class="section-body">band, dancers from different continents</p>
  </section>

  <section class="section">
    <h2 class="section-title">Visual Film Footage:</h2>
    <p class="section-body">Travel show showing beautiful destinations.</p>
  </section>

  <section class="section">
    <h2 class="section-title">Display:</h2>
    <p class="section-body">On display could be planes from the different decades</p>
  </section>

  <section class="section">
    <h2 class="section-title">Food / Table Display:</h2>
    <p class="section-body">Buffet with food from around the world ie Mexican, Greek, Italian etc</p>
  </section>

  <section class="section">
    <h2 class="section-title">Entertainment</h2>
    <p class="section-body">Photo Booth - for your passport photos with fun things to wear for the<br>photos<br>Baggage tags for a mystery draw and to receive a individually num-<br>bered small cardboard suitcase with a few fun dress up items inside<br>(eg mastaches, hats, glasses) to get people less inhibited and in a par-<br>ty spirit.</p>
  </section>
</main>
</body>
</html>
```